Business card design

Need a business card design. Two sided.

My company's name is RAV3 CONSULTANTS. C for Creative, U for Unified, E for Exuberance. 8 simbolizes infinity.

Business is focused on business brokering, business solutions and venture capitalization

More projects will be given for the awarded contestant for web design, brochure design in the future.

Attached is the initial logo that was given to me. Use as reference but am definitely open to new ideas. I want something that is simple but stands out.

```html
<!DOCTYPE html>
<html lang="en">
<head>
<meta charset="utf-8">
<title>RAV3 Consultants – Business Card</title>
<link rel="stylesheet" href="https://fonts.googleapis.com/css2?family=Ubuntu:wght@400;500;700&display=swap">
<style>
  :root {
    --backdrop: #2a2a2a;
    --card-white: #ffffff;
    --brand-red: #8e1d22;
    --brand-red-light: #b3333a;
    --brand-red-dark: #5e0f13;
    --ink-grey: #6d6d6d;
    --ink-dark: #333333;
    --rule-grey: #c9c9c9;
  }
  * { box-sizing: border-box; margin: 0; padding: 0; }
  html, body { width: 1200px; height: 769px; overflow: hidden; }
  body {
    background: var(--backdrop);
    font-family: "Ubuntu", sans-serif;
    position: relative;
  }
  .card {
    position: absolute;
    top: 234px;
    width: 520px;
    height: 300px;
    overflow: hidden;
    border-radius: 3px;
  }
  .card-front { left: 50px; background: var(--card-white); }
  .card-back {
    left: 630px;
    background: linear-gradient(160deg, var(--brand-red-light) 0%, var(--brand-red) 45%, var(--brand-red-dark) 100%);
    color: var(--card-white);
  }

  /* front */
  .front-band { position: absolute; inset: 0; }
  .brand {
    position: absolute;
    top: 44px;
    right: 40px;
    display: flex;
    align-items: center;
    gap: 10px;
  }
  .brand-dot {
    width: 30px; height: 30px; border-radius: 50%;
    background: var(--brand-red);
  }
  .brand-name {
    font-weight: 700;
    font-size: 26px;
    letter-spacing: 0.5px;
    color: var(--brand-red);
  }
  .person {
    position: absolute;
    top: 100px;
    right: 40px;
    text-align: right;
  }
  .person-name { font-weight: 700; font-size: 19px; color: var(--brand-red); }
  .person-title { font-weight: 500; font-size: 14px; color: var(--ink-dark); margin-top: 2px; }
  .divider {
    position: absolute;
    top: 150px; left: 40px; right: 40px;
    height: 1px; background: var(--rule-grey);
  }
  .contacts {
    position: absolute;
    left: 40px;
    top: 162px;
    list-style: none;
    font-size: 12.5px;
    color: var(--ink-dark);
  }
  .contacts li { display: flex; align-items: center; gap: 8px; line-height: 20px; }
  .contacts svg { width: 12px; height: 12px; fill: var(--ink-dark); flex: none; }
  .front-web {
    position: absolute;
    right: 40px;
    bottom: 18px;
    font-size: 13px;
    color: var(--card-white);
  }

  /* back */
  .back-brand {
    position: absolute;
    top: 82px; left: 0; right: 0;
    display: flex; flex-direction: column; align-items: center; gap: 14px;
  }
  .back-dot {
    width: 64px; height: 64px; border-radius: 50%;
    background: var(--card-white);
  }
  .back-name { font-weight: 700; font-size: 30px; letter-spacing: 0.5px; color: var(--card-white); }
  .back-web {
    position: absolute;
    bottom: 46px; left: 0; right: 0;
    display: flex; justify-content: center; align-items: center; gap: 10px;
    font-size: 14px;
  }
  .dots { display: flex; gap: 4px; align-items: center; }
  .dots span { width: 5px; height: 5px; border-radius: 50%; background: var(--card-white); }
  .dots span:nth-child(3) { width: 7px; height: 7px; }
</style>
</head>
<body>

<section class="card card-front" aria-label="Business card front">
  <svg class="front-band" viewBox="0 0 520 300" preserveAspectRatio="none" aria-hidden="true">
    <path d="M0 300 L0 292 C120 292 170 258 230 252 C300 246 420 250 520 246 L520 300 Z" fill="var(--rule-grey)"/>
    <path d="M0 300 C120 298 180 266 240 260 C310 254 420 256 520 252 L520 300 Z" fill="var(--brand-red)"/>
  </svg>

  <div class="brand">
    <span class="brand-dot"></span>
    <span class="brand-name">RAV3 CONSULTANTS</span>
  </div>

  <div class="person">
    <p class="person-name">Daniel Hofer</p>
    <p class="person-title">Managing Director</p>
  </div>

  <div class="divider"></div>

  <ul class="contacts">
    <li>
      <svg viewBox="0 0 12 12"><path d="M2 1 L4.5 1 L5.5 3.5 L4 4.5 C4.7 6 6 7.3 7.5 8 L8.5 6.5 L11 7.5 L11 10 C6 10.5 1.5 6 2 1 Z"/></svg>
      +41 70 000 12 34
    </li>
    <li>
      <svg viewBox="0 0 12 12"><path d="M1 2.5 H11 V9.5 H1 Z M1.6 3 L6 6.5 L10.4 3" fill="none" stroke="var(--ink-dark)" stroke-width="1.2"/></svg>
      info@rav3consult.ch
    </li>
    <li>
      <svg viewBox="0 0 12 12"><rect x="1" y="1" width="10" height="10" rx="1.5"/></svg>
      www.facebook.com/rav3consult
    </li>
    <li>
      <svg viewBox="0 0 12 12"><path d="M6 0.5 C3.6 0.5 2 2.3 2 4.4 C2 7.3 6 11.5 6 11.5 C6 11.5 10 7.3 10 4.4 C10 2.3 8.4 0.5 6 0.5 Z M6 3 A1.5 1.5 0 1 0 6 6 A1.5 1.5 0 1 0 6 3 Z" fill-rule="evenodd"/></svg>
      Lindenweg 12, 8000 Zürich
    </li>
  </ul>

  <p class="front-web">www.domain.com</p>
</section>

<section class="card card-back" aria-label="Business card back">
  <div class="back-brand">
    <span class="back-dot"></span>
    <span class="back-name">RAV3 CONSULTANTS</span>
  </div>
  <div class="back-web">
    <span class="dots"><span></span><span></span><span></span></span>
    <span>www.yoursite.com</span>
    <span class="dots"><span></span><span></span><span></span></span>
  </div>
</section>

</body>
</html>
```